Online Prescription Eyeglass Lens Company Needs a Website

*Update new name to ClearPair. Thx

We are eye doctors with a lab that need a website for a new company based in Southern California called ClearPair. We replace old prescription lenses with new ones next day for most lenses. Patients select the lenses and give us the prescription. We then send a box with a prepaid shipping label. Place the frames in the box and drop them in the mail to our lab. We will custom make new lenses, fit them back into your frames and send them back to you. We would like to compete with www.vizora.com and offer affordable lenses for single vision, bifocal, progressive, sunglass lenses at an affordable price with next day shipping.
Updates

Hi Designers, We have a new name called ClearPair. Can we have the website design reflect the new name and we'll pick our favorites. Thx

Update: The new name is OptiNova . I have not made very many changes or feedback to the submissions because we were bidding for a .com. We won and our new name is OptiNova . This is the last name change.. Please have the website reflect the new name and I'll be providing feedback on the websites . ( I have a separate project for the logo people are working on, so don't worry about creating a logo). Look forward to the submissions. Thanks everyone.

Hi, Just leave the name as ClearPair for now. I will narrow down top designs tonight. Thx

Target Market(s)

Anyone that wears prescription or nonprescription glasses or sunglasses that want next day shipping.

Industry/Entity Type

Eyewear

Number of Pages Required

4 page

Font styles to use
Serif

Colors

Designer to choose colors to be used in the design.

Requirements
Must have
• I need a website that can compete with https://www.vizora.com/.
• We are different from vizora because we can offer same day service or next day shipping.
• It needs to have website that offers the lenses available listed below.
• Needs to be able to upload a prescription and payment feature.
• Pictures of different types of options with small info about each lens option.
• Template Pricing (just use numbers from $79-$179 for now)
• SINGLE VISION LENSES
• HIGH INDEX LENSES
• READING LENSES
• DIGITAL HD PROGRESSIVE LENSES
• RX & NON-RX SUNGLASSES
• RX & NON-RX POLARIZED SUNGLASSES
• COMPUTER LENSES
• TRANSITION LENSES
• BI-FOCAL LENSES

```html
<!DOCTYPE html>
<html lang="en">
<head>
<meta charset="utf-8">
<title>ClearPair — Prescription Lenses</title>
<link rel="stylesheet" href="https://fonts.googleapis.com/css2?family=Crimson+Text:wght@400;600;700&family=Oswald:wght@600&family=Roboto:wght@400;500;700&display=swap">
<style>
:root{
  --green:#3a9b3c;
  --green-bright:#56c24a;
  --cyan:#1fcfdc;
  --ink:#1d1d1d;
  --text:#444;
  --grey:#9e9e9e;
  --footer:#0e2b18;
  --white:#fff;
  --serif:'Crimson Text', Georgia, serif;
  --sans:'Roboto', Arial, sans-serif;
  --display:'Oswald', 'Arial Narrow', sans-serif;
}
*{box-sizing:border-box;margin:0;padding:0}
html,body{width:1200px;height:2736px;overflow:hidden;background:#fff}
body{position:relative;font-family:var(--sans);color:var(--text)}
.abs{position:absolute}

/* hero */
.hero-photo{left:0;top:0;width:1200px;height:700px;background:linear-gradient(100deg,#d9e3ea 0%,#b9c9d6 25%,#2c5fb0 38%,#e7ecef 60%,#d7c8b4 82%,#efe5d6 100%)}
.topbar{left:0;top:0;width:1200px;height:115px;background:rgba(58,155,60,.55)}
.brand{left:88px;top:36px;display:flex;align-items:center;gap:14px;font-family:var(--sans);font-weight:700;font-size:30px;color:var(--white)}
.brand-mark{width:22px;height:22px;border-radius:50%;background:var(--cyan)}
.social{right:84px;top:6px;display:flex;gap:16px}
.social span{font-size:12px;color:var(--white);font-weight:500}
.phone{left:606px;top:62px;display:flex;align-items:center;gap:12px;color:var(--white);font-size:16px}
.search{left:784px;top:60px;width:228px;height:24px;border-bottom:1px solid rgba(255,255,255,.85);color:var(--white);font-size:13px;display:flex;justify-content:space-between;align-items:center}
.menu{left:1040px;top:64px;display:flex;align-items:center;gap:12px;color:var(--white);font-size:16px}
.menu i{display:block;width:24px;height:4px;background:var(--white);box-shadow:0 8px 0 var(--white),0 -8px 0 var(--white)}
.hero-title{left:88px;top:438px;background:rgba(10,10,10,.72);padding:0 12px 2px;font-family:var(--display);font-weight:600;font-size:50px;line-height:58px;color:var(--green-bright)}
.hero-sub{left:88px;top:503px;background:rgba(10,10,10,.72);padding:2px 10px;font-family:var(--serif);font-size:26px;line-height:34px;color:var(--white)}
.btn-pill{left:88px;top:565px;width:198px;height:52px;border-radius:26px;background:var(--green);color:var(--white);font-family:var(--serif);font-weight:700;font-size:17px;display:flex;align-items:center;justify-content:center;text-transform:uppercase}

/* lens cards */
.lens-img{top:766px;height:252px}
.lens-img.left{left:0;width:277px;background:linear-gradient(160deg,#3a3d40,#cfd4d8 55%,#8f979d)}
.lens-img.right{left:921px;width:279px;background:linear-gradient(180deg,#2d6fd2 0%,#8fb7e8 45%,#9c9a94 60%,#3e3f42 100%)}
.lens-card{top:766px;width:314px;height:252px;border:1px solid #cfcfcf;background:#fff}
.lens-card.one{left:277px}
.lens-card.two{left:607px}
.lens-card h3{position:absolute;left:18px;top:32px;font-family:var(--sans);font-weight:500;font-size:19px;color:#2a2a2a}
.lens-card hr{position:absolute;left:18px;top:68px;width:36px;border:0;border-top:2px solid var(--green)}
.lens-card p{position:absolute;left:18px;top:78px;width:280px;font-size:13px;line-height:22px;color:#555}
.price{position:absolute;top:214px;height:37px;display:flex}
.price span{display:flex;align-items:center;justify-content:center;color:#fff;font-size:17px}
.price .amt{width:117px;background:var(--grey);font-weight:500}
.price .order{width:122px;background:var(--green);font-family:var(--serif);font-size:17px}
.nub{width:0;height:0;border-top:12px solid transparent;border-bottom:12px solid transparent;top:880px}
.arrow{top:862px;width:26px;height:56px;background:rgba(255,255,255,.6);display:flex;align-items:center;justify-content:center}

/* process */
.section-title{font-family:var(--serif);font-weight:600;color:var(--ink);text-align:center;width:1200px;left:0}
.process-title{top:1074px;font-size:34px}
.rule{width:54px;height:2px;background:var(--green)}
.step{top:1150px;width:360px;text-align:center}
.step p{margin-top:28px;font-family:var(--serif);font-size:21px;line-height:27px;color:#222}

/* about */
.about-photo{left:0;top:1527px;width:600px;height:397px;background:linear-gradient(110deg,#2f3b3c 0%,#b8c5c9 30%,#eef2f3 55%,#d9c3b2 75%,#f0eeea 100%)}
.about-box{left:560px;top:1580px;width:640px;height:344px;background:var(--cyan);color:var(--white);padding:30px 44px}
.about-box h2{font-family:var(--serif);font-weight:600;font-size:37px;line-height:42px}
.about-box .rule{background:#fff;margin:8px 0 16px}
.about-box p{font-size:12.5px;line-height:22px;width:525px}
.btn-outline{margin-top:30px;width:212px;height:44px;border:1.5px solid #1b3b3d;border-radius:22px;display:flex;align-items:center;justify-content:center;font-family:var(--serif);font-weight:700;font-size:18px;color:#1b2b2c}

/* newsletter */
.news-title{top:1980px;font-size:31px}
.news-form{left:305px;top:2050px;display:flex}
.news-input{width:450px;height:48px;border:1px solid #c9c9c9;border-right:0;border-radius:24px 0 0 24px;padding-left:26px;display:flex;align-items:center;font-size:13px;color:#888}
.news-btn{width:141px;height:48px;border-radius:0 24px 24px 0;background:var(--green);color:#fff;font-family:var(--serif);font-weight:700;font-size:21px;display:flex;align-items:center;justify-content:center}

/* promo panels */
.promo{top:2165px;width:600px;height:370px;padding:62px 0 0 88px;color:#fff}
.promo.glasses{left:0;background:linear-gradient(120deg,#4f6a40,#6d7c54 50%,#50623e)}
.promo.sun{left:600px;padding-left:26px;background:linear-gradient(120deg,#2fb6b9,#27a3ab 55%,#1f8992)}
.promo h2{font-family:var(--serif);font-weight:600;font-size:32px;line-height:36px;text-transform:uppercase;letter-spacing:.5px}
.promo .rule{background:#2b3b36;width:64px;margin:8px 0 14px}
.promo.glasses .rule{visibility:hidden}
.promo p{width:490px;font-size:12.5px;line-height:23px;text-align:justify}
.btn-shop{margin-top:30px;width:116px;height:36px;border-radius:18px;background:var(--cyan);display:flex;align-items:center;justify-content:center;font-size:14px;font-weight:500;text-transform:uppercase}

/* footer */
.footer{left:0;top:2603px;width:1200px;height:87px;background:var(--footer);color:#fff;font-size:15px}
.footer .contact{position:absolute;top:32px;display:flex;align-items:center;gap:14px}
.pay{position:absolute;right:88px;top:34px;display:flex;gap:18px;align-items:center}
.pay span{font-size:13px;font-weight:700;color:#fff}
.copy{top:2706px;left:0;width:1200px;text-align:center;font-size:12px;color:#666}
</style>
</head>
<body>

<!-- hero -->
<div class="abs hero-photo" role="img" aria-label="Optometrist examining a patient at an eye testing instrument"></div>
<div class="abs topbar"></div>
<div class="abs brand"><span class="brand-mark"></span>ClearPair</div>
<div class="abs social"><span>Vostiq</span><span>Zembro</span><span>Kalvix</span><span>Ormuna</span></div>
<div class="abs phone">
  <svg width="24" height="22" viewBox="0 0 24 22" fill="#fff"><path d="M2 6c0-3 4-5 10-5s10 2 10 5v2h-5V6H7v2H2z"/><rect x="4" y="10" width="16" height="10" rx="2"/><circle cx="12" cy="15" r="3" fill="rgba(58,155,60,.9)"/></svg>
  555-201-4870
</div>
<div class="abs search"><span>Search...</span>
  <svg width="14" height="14" viewBox="0 0 14 14" fill="none" stroke="#fff" stroke-width="2"><circle cx="6" cy="6" r="4.5"/><path d="M9.5 9.5L13 13"/></svg>
</div>
<div class="abs menu">Menu <i></i></div>
<div class="abs hero-title">We are different</div>
<div class="abs hero-sub">We offer same day service or next day shipping.</div>
<div class="abs btn-pill">See Collection</div>

<!-- lens cards -->
<div class="abs lens-img left" role="img" aria-label="Clear prescription lens resting on a reflective surface"></div>
<div class="abs lens-card one">
  <h3>SINGLE VISION LENSES</h3><hr>
  <p>Lorem Ipsum is simply dummy text of the printing and typesetting industry. Lorem Ipsum has been the industry's standard dummy text ever since when an unknown printer took a galley of type and scrambled</p>
  <div class="price" style="left:74px"><span class="amt">$79</span><span class="order">Order Now</span></div>
</div>
<div class="abs nub" style="left:265px;border-right:12px solid #fff"></div>
<div class="abs lens-card two">
  <h3>RX &amp; NON-RX SUNGLASSES</h3><hr>
  <p>Lorem Ipsum is simply dummy text of the printing and typesetting industry. Lorem Ipsum has been the industry's standard dummy text ever since when an unknown printer took a galley of type and scrambled</p>
  <div class="price" style="left:74px"><span class="amt">$79</span><span class="order">Order Now</span></div>
</div>
<div class="abs nub" style="left:921px;border-left:12px solid #fff"></div>
<div class="abs lens-img right" role="img" aria-label="Dark sunglass lens held against a sunny open road"></div>
<div class="abs arrow" style="left:0"><svg width="10" height="22" viewBox="0 0 10 22" fill="none" stroke="#666" stroke-width="1.5"><path d="M9 1L1 11l8 10"/></svg></div>
<div class="abs arrow" style="left:1174px"><svg width="10" height="22" viewBox="0 0 10 22" fill="none" stroke="#666" stroke-width="1.5"><path d="M1 1l8 10-8 10"/></svg></div>

<!-- process -->
<h2 class="abs section-title process-title">Our Process</h2>
<div class="abs rule" style="left:573px;top:1127px"></div>

<div class="abs step" style="left:66px">
  <svg width="220" height="220" viewBox="0 0 220 220">
    <path d="M110 2L218 110 110 218 2 110z" fill="none" stroke="var(--cyan)" stroke-width="1.5"/>
    <path d="M110 20L200 110 110 200 20 110z" fill="var(--cyan)"/>
    <rect x="84" y="80" width="52" height="64" rx="5" fill="none" stroke="#fff" stroke-width="5"/>
    <rect x="96" y="72" width="28" height="14" rx="3" fill="#fff"/>
    <path d="M110 96v20M100 106h20" stroke="#fff" stroke-width="5"/>
    <path d="M96 128h28M96 136h20" stroke="#fff" stroke-width="3"/>
  </svg>
  <p>We replace old prescription lenses<br>with new ones next day<br>for most lenses</p>
</div>
<div class="abs step" style="left:418px">
  <svg width="220" height="220" viewBox="0 0 220 220">
    <path d="M110 2L218 110 110 218 2 110z" fill="none" stroke="var(--cyan)" stroke-width="1.5"/>
    <path d="M110 20L200 110 110 200 20 110z" fill="var(--cyan)"/>
    <ellipse cx="110" cy="112" rx="40" ry="16" fill="none" stroke="#fff" stroke-width="4"/>
    <path d="M76 104c10-22 58-28 72-10" fill="none" stroke="#fff" stroke-width="4"/>
    <path d="M88 116c14 6 30 6 44 0" fill="none" stroke="#fff" stroke-width="3"/>
  </svg>
  <p>Patients select the lenses and give<br>us the prescription.</p>
</div>
<div class="abs step" style="left:772px">
  <svg width="220" height="220" viewBox="0 0 220 220">
    <path d="M110 2L218 110 110 218 2 110z" fill="none" stroke="var(--cyan)" stroke-width="1.5"/>
    <path d="M110 20L200 110 110 200 20 110z" fill="var(--cyan)"/>
    <path d="M110 72l36 16v42l-36 18-36-18V88z" fill="#fff"/>
    <path d="M74 88l36 16 36-16M110 104v44" fill="none" stroke="var(--cyan)" stroke-width="4"/>
  </svg>
  <p>We then send a box with a prepaid<br>shipping label.</p>
</div>

<!-- about -->
<div class="abs about-photo" role="img" aria-label="Eye doctor checking a smiling patient's eyes in a clinic"></div>
<div class="abs about-box">
  <h2>About ClearPair</h2>
  <div class="rule"></div>
  <p>Sed ut perspiciatis unde omnis iste natus error sit voluptatem accusantium doloremque laudantium, totam rem aperiam, eaque ipsa quae ab illo inventore veritatis et quasi architecto beatae vitae dicta sunt explicabo. Nemo enim ipsam voluptatem quia voluptas sit aspernatur aut odit aut fugit, sed quia consequuntur magni dolores eos qui ratione architecto beatae vitae dicta sunt explicabo. Nemo enim ipsam voluptatem quia voluptas sit aspernatur aut odit aut fugit, sed quia consequuntur magni dolores eos qui ratione</p>
  <div class="btn-outline">Upload a Prescription</div>
</div>

<!-- newsletter -->
<h2 class="abs section-title news-title">Subscribe Our Newsletter</h2>
<div class="abs news-form">
  <div class="news-input">Enter your email</div>
  <div class="news-btn">Subscribe</div>
</div>

<!-- promos -->
<div class="abs promo glasses" role="img" aria-label="Young man wearing designer eyeglasses in a bright green setting">
  <h2>Designer Glasses</h2>
  <div class="rule"></div>
  <p>Lorem Ipsum is simply dummy text of the printing and typesetting industry. Lorem Ipsum has been the industry's standard dummy text ever since the 1500s, when an unknown printer took a galley of type and scrambled it to make a type specimen book. It has survived not only five centuries, but also the leap into electronic typesetting, remaining essentially unchanged. It was popularised in the</p>
  <div class="btn-shop">Shop Now</div>
</div>
<div class="abs promo sun" role="img" aria-label="Woman wearing designer sunglasses with a teal tint">
  <h2>Designer Sunglasses</h2>
  <div class="rule"></div>
  <p>Lorem Ipsum is simply dummy text of the printing and typesetting industry. Lorem Ipsum has been the industry's standard dummy text ever since the 1500s, when an unknown printer took a galley of type and scrambled it to make a type specimen book. It has survived not only five centuries, but also the leap into electronic typesetting, remaining essentially unchanged. It was popularised in the</p>
  <div class="btn-shop">Shop Now</div>
</div>

<!-- footer -->
<div class="abs footer">
  <div class="contact" style="left:88px">
    <svg width="26" height="20" viewBox="0 0 26 20" fill="none" stroke="#fff" stroke-width="1.5"><rect x="1" y="1" width="24" height="18"/><path d="M1 1l12 10L25 1"/></svg>
    hello@clearpair.com
  </div>
  <div class="contact" style="left:330px">
    <svg width="26" height="22" viewBox="0 0 24 22" fill="#fff"><path d="M2 6c0-3 4-5 10-5s10 2 10 5v2h-5V6H7v2H2z"/><rect x="4" y="10" width="16" height="10" rx="2"/><circle cx="12" cy="15" r="3" fill="#0e2b18"/></svg>
    555.310.7725
  </div>
  <div class="pay"><span>Pavinzo</span><span>Crelmar</span><span>Visquo</span><span>Tandrel</span><span>Dorvisk</span><span>Ambrexo</span></div>
</div>
<div class="abs copy">© 2017 company name. All rights reserved</div>

</body>
</html>
```